Business Card Design Project

Business card design using our logo, consistent with website branding (www.brightvane.com.au) and includes our services:

advertising|sales|events|production

Details Required:

Dorian Webb
Managing Director

P 1300 586 231
M 0404 827 659
F (02) 9613 2048
E dorian@brightvane.com.au
W www.brightvane.com.au

Will be printed on high quality card with rounded corners.

Quick turnaround required, on standby for any questions to assist with this.

Will upload logo and previous drafts we didn't think were the right fit.

Target Market(s)

Senior business decision-makers

Industry/Entity Type

Business

Requirements
Must have
• Editable template, so details can be updated for staff

Must be in print ready format - please see specs I have just uploaded

```html
<!DOCTYPE html>
<html lang="en">
<head>
<meta charset="utf-8">
<title>BrightVane Business Card</title>
<link rel="stylesheet" href="https://fonts.googleapis.com/css2?family=Questrial&family=Roboto:wght@400;700&display=swap">
<style>
  :root {
    --bg-dark: #3a3a3a;
    --bg-light: #4d4d4d;
    --orange: #f7931e;
    --orange-text: #f39a2b;
    --red: #ec3a36;
    --blue: #1a8fd8;
    --blue-deep: #0f77c2;
    --white: #ffffff;
    --paper: #fbfbfb;
  }
  * { box-sizing: border-box; margin: 0; padding: 0; }
  html, body { width: 1200px; height: 900px; overflow: hidden; }
  body {
    background: radial-gradient(ellipse at 50% 40%, var(--bg-light), var(--bg-dark));
    position: relative;
    font-family: "Questrial", sans-serif;
  }
  .card {
    position: absolute;
    left: 240px;
    width: 722px;
    height: 410px;
    border-radius: 18px;
    overflow: hidden;
    box-shadow: 0 6px 18px rgba(0,0,0,0.45);
  }
  .card-front {
    top: 24px;
    background: linear-gradient(90deg, var(--orange) 0%, #f36f2a 55%, var(--red) 100%);
    display: flex;
    align-items: center;
    justify-content: center;
    gap: 22px;
  }
  .brand-dot {
    width: 96px; height: 96px;
    border-radius: 50%;
    background: var(--white);
  }
  .brand-name {
    color: var(--white);
    font-size: 66px;
    letter-spacing: -0.5px;
  }
  .card-back {
    top: 464px;
    height: 412px;
    background: var(--paper);
  }
  .name-band {
    position: absolute;
    left: 0; top: 0; bottom: 0;
    width: 142px;
    background: linear-gradient(180deg, var(--blue) 0%, var(--blue-deep) 100%);
    display: flex;
    align-items: flex-end;
    justify-content: center;
    gap: 4px;
    padding-bottom: 22px;
  }
  .name-band span {
    writing-mode: vertical-rl;
    transform: rotate(180deg);
    color: var(--white);
    font-family: "Roboto", sans-serif;
    white-space: nowrap;
  }
  .person-name { font-weight: 700; font-size: 38px; }
  .person-title { font-weight: 400; font-size: 33px; }
  .contact-list {
    position: absolute;
    left: 164px;
    top: 118px;
    list-style: none;
  }
  .contact-list li {
    display: flex;
    align-items: center;
    height: 56px;
    color: var(--orange-text);
    font-size: 34px;
  }
  .contact-list svg {
    width: 30px; height: 30px;
    margin-right: 14px;
    fill: var(--blue);
    flex: none;
  }
  .back-brand {
    position: absolute;
    right: 40px;
    top: 120px;
    color: var(--orange-text);
    font-size: 34px;
  }
</style>
</head>
<body>
  <section class="card card-front">
    <div class="brand-dot"></div>
    <div class="brand-name">BrightVane</div>
  </section>

  <section class="card card-back">
    <div class="name-band">
      <span class="person-name">Dorian Webb</span>
      <span class="person-title">Managing Director</span>
    </div>

    <div class="back-brand">BrightVane</div>

    <ul class="contact-list">
      <li>
        <svg viewBox="0 0 24 24"><path d="M6.6 10.8a15 15 0 0 0 6.6 6.6l2.2-2.2c.3-.3.7-.4 1-.2 1.1.4 2.3.6 3.6.6.6 0 1 .4 1 1V20c0 .6-.4 1-1 1A17 17 0 0 1 3 4c0-.6.4-1 1-1h3.5c.6 0 1 .4 1 1 0 1.3.2 2.5.6 3.6.1.3 0 .7-.2 1z"/></svg>
        1300.586.231
      </li>
      <li>
        <svg viewBox="0 0 24 24"><path d="M6 2h9l3 3v4H6zM3 10h18a1 1 0 0 1 1 1v7a1 1 0 0 1-1 1h-2v-4H5v4H3a1 1 0 0 1-1-1v-7a1 1 0 0 1 1-1zm4 6h10v6H7z"/></svg>
        (02) 9613.2048
      </li>
      <li>
        <svg viewBox="0 0 24 24"><path d="M8 1h8a2 2 0 0 1 2 2v18a2 2 0 0 1-2 2H8a2 2 0 0 1-2-2V3a2 2 0 0 1 2-2zm0 3v11h8V4zm4 13a1.5 1.5 0 1 0 0 3 1.5 1.5 0 0 0 0-3z"/></svg>
        0404.827.659
      </li>
      <li>
        <svg viewBox="0 0 24 24"><path d="M2 6a2 2 0 0 1 2-2h16a2 2 0 0 1 2 2v.5l-10 6-10-6zm0 3 10 6 10-6v9a2 2 0 0 1-2 2H4a2 2 0 0 1-2-2z"/></svg>
        dorian@brightvane.com.au
      </li>
      <li>
        <svg viewBox="0 0 24 24"><path d="M4 2l16 9-7 1.5 4 8-3 1.5-4-8L4 19z"/></svg>
        www.brightvane.com.au
      </li>
    </ul>
  </section>
</body>
</html>
```